Yoga Workshop - Yoga Practice information flyer

I am a yoga teacher who will be presenting a workshop on yoga for sleep and need a brochure for my clients which outlines a practice that I give them so they can do the practice at home. Ideally I would like a brochure that is a single A3 size of paper in size that folds in half to an A4 booklet with the entire practice on the centre section to make it easy for people to do the practice at home with just one open page in front of them:
* Front page detailing "Yoga for Sleep Workshop" and "Restorative Yoga Practice"
* Centre contains the information on the practice contained in the attached word document. The practice consists of 5 postures, so there needs to be five separate sections which have the pictures of the postures (attached in uploaded files) and the wording contained in the attached word document. All pictures uploaded need to be included in the flyer as each posture has different pictures demonstrating the posture using yoga props or using things people have at home
* Back page containing a picture of myself (picture uploaded in files) with some information about me (contained in the attached word document) and my website www.lumaverisk.com.au

I also need this flyer to be able to printed on 2 double sided A4 sheets of paper so will require 2 x pdf file versions. Importantly, for the centre section of the flyer, the design needs to ensure if it is printed on A4 paper, the wording and pictures for each of the postures are not separated over two pages

Target Market(s)

Existing clients

Requirements
Must have
• Detailed in project description
Nice to have
• The word document also contains some quotes. These do not need to be included in the flyer. If there is room and there is room for one or two of those please include where it would look good
Should not have
• Stock pictures of people in yoga postures which a normal everyday person could not get into

```html
<!DOCTYPE html>
<html lang="en">
<head>
<meta charset="utf-8">
<title>Yoga for Sleep Workshop – Brochure</title>
<link href="https://fonts.googleapis.com/css2?family=Lora:wght@700&family=Josefin+Sans:wght@400&family=Roboto:wght@400;500;700&family=Roboto+Condensed:wght@400;700&family=Dancing+Script:wght@500&display=swap" rel="stylesheet">
<style>
:root{
  --bg:#e4e4e4;
  --paper:#ffffff;
  --orange:#cf8a5c;
  --navy:#2f3f5c;
  --panel:#ececec;
  --floor-a:#8a4f2c;
  --floor-b:#2a8fb8;
}
*{margin:0;padding:0;box-sizing:border-box}
html,body{width:1200px;height:2784px;overflow:hidden;background:var(--bg)}
body{position:relative;font-family:'Roboto',sans-serif;color:var(--navy)}
.page{position:absolute;background:var(--paper);box-shadow:0 6px 18px rgba(0,0,0,.12)}

/* cover & back */
.cover{width:430px;height:608px;display:flex;flex-direction:column;align-items:center;padding-top:40px}
.brand{display:flex;flex-direction:column;align-items:center;gap:6px}
.brand-dot{width:30px;height:30px;border-radius:50%;border:2px solid var(--orange)}
.brand-name{font-family:'Lora',serif;font-weight:700;font-size:20px;color:var(--navy)}
.brand-tag{font-family:'Josefin Sans',sans-serif;font-size:7.5px;letter-spacing:.8px;color:var(--navy)}
.drop{margin-top:18px;width:280px;height:318px}
.cover-title{margin-top:18px;font-family:'Roboto',sans-serif;font-size:19px;line-height:26px;text-align:center;color:var(--navy);font-weight:400}
.url-band{margin-top:8px;width:300px;height:24px;border-radius:12px;background:var(--orange);color:#fff;font-size:13px;font-weight:500;letter-spacing:3px;display:flex;align-items:center;justify-content:center}
.back{width:430px;height:608px;display:flex;flex-direction:column;align-items:center;padding-top:170px}
.portrait{width:150px;height:150px;border-radius:50%;border:2px solid var(--orange);padding:4px}
.portrait div{width:100%;height:100%;border-radius:50%;background:linear-gradient(160deg,#6f9a4c,#9ab7d0 70%,#5c7fa8)}
.about-title{margin-top:12px;width:200px;border-top:1px solid var(--navy);padding-top:4px;text-align:center;font-size:13px;font-weight:700}
.about-text{margin-top:8px;width:245px;font-size:7px;line-height:9px;text-align:justify;text-align-last:center}
.back .brand{margin-top:auto}
.back .brand-dot{width:18px;height:18px}
.back .brand-name{font-size:11px}
.back .brand-tag{font-size:4.5px;letter-spacing:.4px}
.back .url-band{margin:10px 0 36px}

/* inner spread */
.inner{width:540px;height:764px;padding:30px 34px}
.intro{font-family:'Roboto Condensed',sans-serif;font-weight:700;font-size:10.5px;line-height:13px;text-transform:uppercase;margin-bottom:12px}
.intro p+p{margin-top:10px}
.posture{display:flex;gap:10px;border:1px solid var(--orange);padding:8px;margin-bottom:12px;height:178px}
.posture-photo{width:135px;flex:none;background:linear-gradient(180deg,var(--floor-a),#b06a3c 55%,var(--floor-b))}
.posture-photo.wall{background:linear-gradient(180deg,#f2f2f2 40%,var(--floor-a) 70%,var(--floor-b))}
.posture-panel{flex:1;background:var(--panel);padding:14px 12px}
.posture-num{font-size:17px;font-weight:400;color:var(--navy)}
.posture-name{display:inline-block;margin:4px 0 6px;background:var(--orange);color:#fff;font-size:8.5px;font-weight:700;border-radius:0 10px 10px 0;padding:3px 14px 3px 6px;text-transform:uppercase}
.note-label{font-size:6.5px;font-weight:700;text-transform:uppercase}
.note{font-size:6.5px;line-height:8.5px;margin-bottom:5px}
.quotes{display:grid;grid-template-columns:1fr 1fr;gap:14px;margin-top:14px}
.quote{border:1px solid var(--navy);height:150px;display:flex;flex-direction:column;align-items:center;justify-content:center;text-align:center;padding:26px 14px 10px;position:relative}
.quote-mark{position:absolute;top:-16px;left:50%;transform:translateX(-50%);width:32px;height:32px;border-radius:50%;background:var(--orange);color:#fff;font-family:'Lora',serif;font-size:26px;line-height:40px;text-align:center}
.quote-text{font-size:8.5px;font-weight:700;line-height:11px}
.quote-by{margin-top:8px;font-family:'Dancing Script',cursive;font-size:12px}
</style>
</head>
<body>

<!-- single front cover -->
<section class="page cover" style="left:385px;top:130px">
  <div class="brand"><span class="brand-dot"></span><span class="brand-name">Lumaveri Yoga</span><span class="brand-tag">Be the change you wish to see in the world</span></div>
  <svg class="drop" viewBox="0 0 300 340" role="img" aria-label="Photo of the teacher sitting cross-legged in meditation on a grassy field">
    <defs><linearGradient id="field1" x1="0" y1="0" x2="0" y2="1"><stop offset="0" stop-color="#e9e9e0"/><stop offset=".3" stop-color="#7f9a58"/><stop offset="1" stop-color="#c9b48c"/></linearGradient></defs>
    <path d="M150 4C205 70 292 130 292 210C292 285 228 336 150 336C72 336 8 285 8 210C8 130 95 70 150 4Z" fill="url(#field1)" stroke="#cf8a5c" stroke-width="2"/>
  </svg>
  <h1 class="cover-title">YOGA FOR SLEEP WORKSHOP &amp;<br>RESTORATIVE YOGA SLEEP SEQUENCE</h1>
  <div class="url-band">www.lumaverisk.com.au</div>
</section>

<!-- outer spread: back + front -->
<section class="page back" style="left:170px;top:1060px">
  <div class="portrait" role="img" aria-label="Portrait photo of the teacher"><div></div></div>
  <h2 class="about-title">ABOUT THE TEACHER</h2>
  <p class="about-text">Mira Elden is a current serving Naval Officer, Certified Yoga Therapist and RestWell Level 2 instructor. Mira's classes are about using the practices and teaching of Yoga to come to the essence of your true self and learning to tap into the internal wisdom which is always present. Mira is dedicated to making the resilience developing practices of Yoga accessible to all Australian Military personnel and their families.</p>
  <div class="brand"><span class="brand-dot"></span><span class="brand-name">Lumaveri Yoga</span><span class="brand-tag">Be the change you wish to see in the world</span></div>
  <div class="url-band">www.lumaverisk.com.au</div>
</section>
<section class="page cover" style="left:600px;top:1060px">
  <div class="brand"><span class="brand-dot"></span><span class="brand-name">Lumaveri Yoga</span><span class="brand-tag">Be the change you wish to see in the world</span></div>
  <svg class="drop" viewBox="0 0 300 340" role="img" aria-label="Photo of the teacher sitting cross-legged in meditation on a grassy field">
    <defs><linearGradient id="field2" x1="0" y1="0" x2="0" y2="1"><stop offset="0" stop-color="#e9e9e0"/><stop offset=".3" stop-color="#7f9a58"/><stop offset="1" stop-color="#c9b48c"/></linearGradient></defs>
    <path d="M150 4C205 70 292 130 292 210C292 285 228 336 150 336C72 336 8 285 8 210C8 130 95 70 150 4Z" fill="url(#field2)" stroke="#cf8a5c" stroke-width="2"/>
  </svg>
  <h1 class="cover-title">YOGA FOR SLEEP WORKSHOP &amp;<br>RESTORATIVE YOGA SLEEP SEQUENCE</h1>
  <div class="url-band">www.lumaverisk.com.au</div>
</section>

<!-- inner spread -->
<section class="page inner" style="left:60px;top:1900px">
  <div class="intro">
    <p>Use this sequence to relax and unwind at the end of a day or before bed. Settle comfortably into each posture for about 5-7 minutes. Set a timer to let you know when it is time to change position, and you can also listen to any music you find relaxing at the same time. The audio recording from the yoga for sleep workshop can also be used to recreate the practice at home.</p>
    <p>In the middle of the night when you can't sleep you might like to try getting up and resting in any one of these postures for about 5-10 minutes before heading back to bed.</p>
  </div>
  <article class="posture">
    <div class="posture-photo" role="img" aria-label="Photo of supported chest opening posture with knee support"></div>
    <div class="posture-panel">
      <h3 class="posture-num">POSTURE 1</h3>
      <span class="posture-name">Supported chest opening with knee support</span>
      <p class="note"><span class="note-label">Set up notes</span><br>Place the props in a T-position with one bolster along the mat and one across it. Lie back so the bolster supports the spine and the head rests comfortably.</p>
      <p class="note"><span class="note-label">Caution</span><br>If any lower back pain is felt, lower the bolster height using a folded towel or blanket.</p>
    </div>
  </article>
  <article class="posture">
    <div class="posture-photo" role="img" aria-label="Photo of supported bound-angle posture"></div>
    <div class="posture-panel">
      <h3 class="posture-num">POSTURE 2</h3>
      <span class="posture-name">Supported bound-angle pose</span>
      <p class="note"><span class="note-label">Set up notes</span><br>Similar to posture 1 without the bolster behind the knees. Bring the soles of the feet together with knees wide, supported by blocks or pillows.</p>
      <p class="note"><span class="note-label">Caution</span><br>If any lower back pain is felt, lower the support height or use a thinner blanket.</p>
    </div>
  </article>
  <article class="posture">
    <div class="posture-photo wall" role="img" aria-label="Photo of elevated legs-up-the-wall posture"></div>
    <div class="posture-panel">
      <h3 class="posture-num">POSTURE 3</h3>
      <span class="posture-name">Elevated legs-up-the-wall pose</span>
      <p class="note"><span class="note-label">Set up notes</span><br>Sit side-on to the wall, then swing the legs up as you lie back. Slide a folded blanket under the sacrum so the hips are gently raised.</p>
      <p class="note"><span class="note-label">Caution</span><br>If any lower back pain is felt, lower the height the hips are raised to.</p>
    </div>
  </article>
</section>

<section class="page inner" style="left:600px;top:1900px">
  <article class="posture">
    <div class="posture-photo" role="img" aria-label="Photo of supported child's pose"></div>
    <div class="posture-panel">
      <h3 class="posture-num">POSTURE 4</h3>
      <span class="posture-name">Supported child's pose</span>
      <p class="note"><span class="note-label">Set up notes</span><br>Rest the torso on a bolster or stacked pillows. Turn the head to one side, then to the other side halfway through.</p>
      <p class="note"><span class="note-label">Caution</span><br>If any knee or hip pain is felt, raise the support under the torso with more pillows.</p>
    </div>
  </article>
  <article class="posture">
    <div class="posture-photo" role="img" aria-label="Photo of basic relaxation posture with knee support"></div>
    <div class="posture-panel">
      <h3 class="posture-num">POSTURE 5</h3>
      <span class="posture-name">Basic relaxation posture with knee support</span>
      <p class="note"><span class="note-label">Set up notes</span><br>Lie on the back with a bolster or pillows under the knees.</p>
    </div>
  </article>
  <div class="quotes">
    <div class="quote"><span class="quote-mark">“</span><p class="quote-text">Posture should be steady<br>and comfortable</p><p class="quote-by">- Teachings of Saren Ilvo -</p></div>
    <div class="quote"><span class="quote-mark">“</span><p class="quote-text">Tension is who you think you are,<br>Relaxation is who you actually are</p><p class="quote-by">- Teachings of Saren Ilvo -</p></div>
    <div class="quote"><span class="quote-mark">“</span><p class="quote-text">Life isn't as serious as the mind<br>makes it out to be</p><p class="quote-by">- Arlen Voss -</p></div>
    <div class="quote"><span class="quote-mark">“</span><p class="quote-text">Watch your thoughts, they become words<br>Watch your words, they become actions<br>Watch your actions, they become habits<br>Watch your habits, they become character<br>Watch your character, for it becomes your destiny</p><p class="quote-by">- Old Valley Verses -</p></div>
  </div>
</section>

</body>
</html>
```